IT support company needs Banner Ad for the top of their quote layout template

We need a banner Ad for the top of our for quote layout template so it is sent out on all our quotes

The banner size must be 827 x 100 pixels - anything larger than 60 KB can cause upload time issues

We have attached our logo and examples of the quote page to see how it looks in the context of the whole page.

Essential elements of the banner
- Must have our logo but this can be changed to be different colours if it makes the design work better i.e. Tidal Grove could be all in white

Colours
- Can use all of our standard colours - Orange, Black, Grey and White

Images
- As a premium IT support company we deal with people and technology so would like to see both of these Incorporated into the banner i.e. people using technology These images could be watermarked or one colour effect.

Look and Feel
- Professional, friendly, people, technology, premium

Target Market
Small business owners and managers

Industry/Entity Type

It Company

```html
<!DOCTYPE html>
<html lang="en">
<head>
<meta charset="utf-8">
<title>Tidal Grove – Quote Banner</title>
<link href="https://fonts.googleapis.com/css2?family=Orbitron:wght@800&family=Michroma&display=swap" rel="stylesheet">
<style>
  :root {
    --page-bg: #6a6a6a;
    --white: #ffffff;
    --orange: #f26a1b;
    --black: #141414;
    --photo-dark: #2d3340;
    --photo-mid: #5d7188;
    --photo-light: #9fc3e0;
    --peach-light: #fde3d6;
    --peach-pink: #fbd0cc;
    --peach-warm: #fcdcc0;
    --text-dark: #2a2a2a;
  }
  * { margin: 0; padding: 0; box-sizing: border-box; }
  html, body { width: 1200px; height: 1200px; overflow: hidden; }
  body { background: var(--page-bg); position: relative; }

  .banner {
    position: absolute;
    left: 47px; top: 534px;
    width: 1104px; height: 134px;
    background: var(--white);
    overflow: hidden;
  }
  .brand-panel {
    position: absolute; left: 0; top: 0;
    width: 331px; height: 134px;
    display: flex; align-items: center; justify-content: center;
    background: var(--white);
  }
  .brand-name {
    font-family: "Orbitron", sans-serif;
    font-weight: 800;
    font-size: 27px;
    letter-spacing: 0.5px;
    color: var(--orange);
    text-transform: uppercase;
    white-space: nowrap;
  }
  .photo-area {
    position: absolute; left: 331px; top: 0;
    width: 400px; height: 134px;
    background:
      radial-gradient(ellipse at 55% 40%, var(--photo-light) 0%, transparent 45%),
      linear-gradient(90deg, var(--photo-mid) 0%, var(--photo-dark) 40%, var(--photo-mid) 75%, var(--photo-dark) 100%);
  }
  .shapes { position: absolute; left: 0; top: 0; }
  .message {
    position: absolute; left: 773px; top: 0;
    width: 331px; height: 134px;
    padding-top: 30px;
  }
  .headline {
    font-family: "Orbitron", sans-serif;
    font-weight: 800;
    font-size: 24px;
    line-height: 30px;
    color: var(--orange);
    text-transform: uppercase;
    white-space: nowrap;
  }
  .tagline {
    margin-top: 5px;
    font-family: "Michroma", sans-serif;
    font-size: 14px;
    color: var(--text-dark);
    white-space: nowrap;
  }
</style>
</head>
<body>
  <div class="banner">
    <div class="brand-panel">
      <span class="brand-name">Tidal Grove</span>
    </div>
    <div class="photo-area" role="img" aria-label="Photo of business people using a laptop, tablet and phone linked by a glowing globe network"></div>
    <svg class="shapes" width="1104" height="134" viewBox="0 0 1104 134" aria-hidden="true">
      <defs>
        <linearGradient id="peach" x1="0" y1="0" x2="1" y2="1">
          <stop offset="0" stop-color="var(--peach-light)"/>
          <stop offset="0.55" stop-color="var(--peach-pink)"/>
          <stop offset="1" stop-color="var(--peach-warm)"/>
        </linearGradient>
      </defs>
      <path class="accent-orange" d="M677 0 L716 0 Q742 62 690 134 L660 134 Q702 70 677 0 Z" fill="var(--orange)"/>
      <path class="accent-black" d="M716 0 L727 0 Q750 68 701 134 L690 134 Q742 62 716 0 Z" fill="var(--black)"/>
      <path class="message-panel" d="M727 0 L1104 0 L1104 134 L701 134 Q750 68 727 0 Z" fill="url(#peach)"/>
    </svg>
    <div class="message">
      <p class="headline">Lorem ipsum<br>dolor sit amet</p>
      <p class="tagline">consectetuer adipiscing elit</p>
    </div>
  </div>
</body>
</html>
```